Dentist's Office needs desktop and mobile website design

This is a turnkey project where we are looking for a bright, elegant, modern website design, both for desktop and mobile. Our existing website is hosted on Google sites. We also require the new design to be set up and fully functional - both desktop and mobile - on Google sites. If Google sites is too limiting, its ok to use a platform like Wix or Squarespace. If using these, we will need you to point our domain to the new Wix site, and hand us the credentials so we can continue to update the site.

We want to continue using our current logo so the new website colors need to go with the logo. Our existing website can be found at www.brightmolar58.com.

We want the new website to have the following pages:
1. Home - similar content to our current home page at http://www.brightmolar58.com

We also have pictures of our office and team that we would like to show up on the home page in a collage, slide show, or some other creative. Pictures can be found here: https://files.vandrobox.net/share?id=7KQ2MPLRZWX4TNBVYHDJ8SCAGEF&usp=sharing

Not all pictures have to be used; use as many as needed.

In addition to the content on our current home page, we would like a small section for dental quotes where we could rotate quotes. Sample quotes can be found at http://www.sayingmeadow.net/dental.html

If above content is too much to fit on one page, it is ok to split into two.

2. Our team - similar to http://www.brightmolar58.com/our-dentist-1 . In addition, we want short bios and pictures of other staff added to this page. Pictures and bios can be found here: https://files.vandrobox.net/share?id=7KQ2MPLRZWX4TNBVYHDJ8SCAGEF&usp=sharing

3. Reviews - similar to http://www.brightmolar58.com/patient-testimonials-1

4. Services - provide a summary of services we provide from http://www.brightmolar58.com/dental-services . No need for detailed pages pages for each treatment we have on our current website.

5. Contact Us - http://www.brightmolar58.com/contact-us

Target Market(s)

local population

Industry/Entity Type

Healthcare

Coding

Coded - Design and coding required

Number of Pages Required

5+ page

Font styles to use
Sans Serif

Requirements
Nice to have
• animated icons would be cool

```html
<!DOCTYPE html>
<html lang="en">
<head>
<meta charset="utf-8">
<title>Goldvale Dental Care</title>
<link href="https://fonts.googleapis.com/css2?family=Roboto:wght@300;400;500;700&family=Dancing+Script:wght@600&display=swap" rel="stylesheet">
<style>
:root{
  --orange:#f08a2e;
  --orange-dark:#d9741c;
  --orange-deep:#c9681a;
  --text:#6a6a6a;
  --text-dark:#3d3d3d;
  --card:#f4f4f4;
  --line:#e4e4e4;
  --footer:#6d6d6d;
  --footer-dark:#5e5e5e;
  --white:#ffffff;
}
*{margin:0;padding:0;box-sizing:border-box}
html,body{width:1200px;height:2560px;overflow:hidden}
body{font-family:'Roboto',Arial,sans-serif;color:var(--text);background:var(--white);position:relative}
.abs{position:absolute}
.brand{display:flex;align-items:center;gap:12px;font-size:30px;font-weight:400;color:var(--orange);letter-spacing:.5px}
.brand-dot{width:30px;height:30px;border-radius:50%;background:var(--orange);flex:none}
/* header */
.site-header{position:absolute;left:0;top:0;width:1200px;height:106px}
.site-header .brand{position:absolute;left:75px;top:34px}
.contact-chip{position:absolute;top:28px;display:flex;align-items:center;gap:14px}
.chip-icon{width:38px;height:38px;border:2px solid var(--orange);border-radius:50%;display:flex;align-items:center;justify-content:center}
.call .label{font-size:12px;font-weight:500;color:var(--text-dark);letter-spacing:.3px}
.call .phone{font-size:21px;font-weight:700;color:var(--orange);margin-top:2px}
.address{font-size:13px;line-height:19px;color:var(--text)}
/* nav */
.main-nav{position:absolute;left:0;top:106px;width:1200px;height:61px;background:var(--orange)}
.main-nav a{position:absolute;top:20px;color:var(--white);font-size:14px;font-weight:500;text-decoration:none;letter-spacing:.3px}
.main-nav a.active{top:13px;padding:0 26px;height:36px;line-height:32px;border:2px solid var(--white);border-radius:18px}
.search{position:absolute;left:877px;top:13px;width:248px;height:36px;border-radius:18px;background:var(--orange-dark)}
.search svg{position:absolute;right:16px;top:10px}
/* hero */
.hero{position:absolute;left:0;top:167px;width:1200px;height:513px;background:linear-gradient(135deg,#5b4a3c 0%,#7a6450 35%,#8d7660 55%,#4f4036 100%)}
.hero-shade{position:absolute;inset:0;background:rgba(0,0,0,.18)}
.hero h1{position:absolute;top:160px;width:100%;text-align:center;color:var(--white);font-weight:300;font-size:46px;letter-spacing:2px}
.hero p{position:absolute;top:218px;width:100%;text-align:center;color:var(--white);font-size:23px;font-weight:400}
.btn{display:inline-block;background:var(--orange);color:var(--white);font-weight:500;text-align:center;border-radius:22px;letter-spacing:.4px}
.hero .btn{position:absolute;left:485px;top:282px;width:230px;height:41px;line-height:41px;font-size:14px}
.dots{position:absolute;top:478px;left:554px;display:flex;gap:12px;align-items:center}
.dots span{width:11px;height:11px;border-radius:50%;background:var(--white)}
.dots span.on{width:18px;height:18px;background:transparent;border:2px solid var(--white)}
/* section heads */
.sec-title{position:absolute;width:100%;text-align:center;color:var(--orange);font-size:34px;font-weight:300}
.sec-lead{position:absolute;left:290px;width:620px;text-align:center;font-size:13px;line-height:19px}
/* services */
.service{position:absolute;top:908px;width:245px;height:263px;background:var(--card);text-align:center}
.service::after{content:"";position:absolute;left:10px;right:10px;bottom:-18px;height:18px;background:radial-gradient(ellipse at top,rgba(0,0,0,.22),rgba(0,0,0,0) 70%)}
.service .icon{position:absolute;left:75px;top:-47px;width:94px;height:94px;border-radius:50%;background:var(--white);border:3px solid var(--orange);display:flex;align-items:center;justify-content:center}
.service h3{position:absolute;top:76px;width:100%;font-size:23px;font-weight:400;color:var(--orange)}
.service p{position:absolute;top:120px;left:22px;right:22px;font-size:13px;line-height:20px;text-align:justify;text-align-last:center}
.service .btn{position:absolute;left:64px;top:198px;width:117px;height:38px;line-height:38px;font-size:12px}
/* welcome */
.welcome{position:absolute;left:0;top:1246px;width:1200px;height:413px;background:var(--orange);color:var(--white);text-align:center}
.welcome h2{position:absolute;top:66px;width:100%;font-size:31px;font-weight:300}
.welcome .rule{position:absolute;left:580px;top:112px;width:40px;height:2px;background:var(--white)}
.welcome .tagline{position:absolute;top:140px;left:300px;width:600px;font-family:'Dancing Script',cursive;font-weight:600;font-size:22px;line-height:27px}
.welcome .body{position:absolute;top:218px;left:85px;width:1030px;font-size:13.5px;line-height:22px}
.welcome .btn-ghost{position:absolute;left:527px;top:304px;width:144px;height:41px;line-height:37px;border:2px solid var(--white);border-radius:21px;font-size:13px;font-weight:500}
/* quotes */
.quote{position:absolute;top:1837px;width:318px;height:116px;background:var(--card);padding:26px 24px 0;text-align:center;font-size:13.5px;line-height:22px}
.quote::after{content:"";position:absolute;left:28px;bottom:-16px;border-left:14px solid transparent;border-right:14px solid transparent;border-top:16px solid var(--card)}
.author{position:absolute;top:1975px;display:flex;align-items:center;gap:16px;font-size:16px;color:var(--orange)}
.avatar{width:62px;height:62px;border-radius:50%;border:3px solid #eaeaea;background:linear-gradient(160deg,#e8d6c8,#b99c86)}
.divider{position:absolute;left:75px;top:2083px;width:1050px;height:1px;background:var(--line)}
/* members */
.member-title{position:absolute;left:75px;top:2130px;font-size:22px;font-weight:300;color:var(--orange)}
.member-text{position:absolute;left:75px;top:2172px;width:500px;font-size:13px;line-height:20px}
.badge{position:absolute;top:2125px;width:152px;height:82px;border:1px solid #dcdcdc;display:flex;align-items:center;justify-content:center}
.badge span{width:96px;height:30px;border-radius:4px;background:#d8dde2}
/* footer */
.site-footer{position:absolute;left:0;top:2257px;width:1200px;height:303px;background:linear-gradient(180deg,var(--footer),var(--footer-dark));color:var(--white)}
.site-footer .brand{position:absolute;left:75px;top:66px;color:var(--white);font-size:24px}
.site-footer .brand-dot{background:var(--white);width:24px;height:24px}
.legal{position:absolute;left:75px;top:150px;font-size:13px;line-height:22px}
.col-title{position:absolute;top:52px;font-size:21px;font-weight:300}
.links{position:absolute;left:358px;top:98px;list-style:none;font-size:13px}
.links li{height:27.5px}
.links li::before{content:"»";margin-right:10px}
.info{position:absolute;left:614px;font-size:13px;line-height:19px;display:flex;gap:12px}
.field{position:absolute;left:913px;width:212px;height:33px;border-radius:17px;background:var(--white);color:#8a8a8a;font-size:12px;line-height:33px;padding-left:22px}
.submit{position:absolute;left:1016px;top:191px;width:109px;height:39px;line-height:39px;font-size:13px}
</style>
</head>
<body>

<header class="site-header">
  <div class="brand"><span class="brand-dot"></span>Goldvale Dental Care</div>
  <div class="contact-chip call" style="left:653px">
    <div class="chip-icon"><svg width="18" height="18" viewBox="0 0 24 24"><path fill="#f08a2e" d="M6.6 10.8a15.1 15.1 0 0 0 6.6 6.6l2.2-2.2c.3-.3.7-.4 1-.2 1.1.4 2.3.6 3.6.6.6 0 1 .4 1 1V20c0 .6-.4 1-1 1A17 17 0 0 1 3 4c0-.6.4-1 1-1h3.5c.6 0 1 .4 1 1 0 1.3.2 2.5.6 3.6.1.3 0 .7-.2 1z"/></svg></div>
    <div><div class="label">CALL US TODAY</div><div class="phone">209-555-0148</div></div>
  </div>
  <div class="contact-chip" style="left:901px">
    <div class="chip-icon"><svg width="16" height="18" viewBox="0 0 24 24"><path fill="#f08a2e" d="M12 2a7 7 0 0 0-7 7c0 5.2 7 13 7 13s7-7.8 7-13a7 7 0 0 0-7-7zm0 9.5A2.5 2.5 0 1 1 12 6.5a2.5 2.5 0 0 1 0 5z"/></svg></div>
    <div class="address">4820 Orchard Row, CA 95390<br>(next to Sunfield Grocers)</div>
  </div>
</header>

<nav class="main-nav">
  <a class="active" style="left:75px">HOME</a>
  <a style="left:206px">OUR TEAM</a>
  <a style="left:335px">REVIEWS</a>
  <a style="left:456px">SERVICES</a>
  <a style="left:584px">CONTACT US</a>
  <div class="search"><svg width="16" height="16" viewBox="0 0 24 24"><circle cx="10" cy="10" r="6.5" fill="none" stroke="#fff" stroke-width="3"/><path d="M15 15l6 6" stroke="#fff" stroke-width="3" stroke-linecap="round"/></svg></div>
</nav>

<section class="hero" role="img" aria-label="Photo of the dentist and assistant treating a patient in the office">
  <div class="hero-shade"></div>
  <h1>BEST DENTAL CARE</h1>
  <p>It’s our genuine care and gentle nature that sets us apart!</p>
  <span class="btn">MAKE AN APPOINTMENT</span>
  <div class="dots"><span class="on"></span><span></span><span></span><span></span></div>
</section>

<h2 class="sec-title" style="top:732px">Our Services</h2>
<p class="sec-lead" style="top:786px">Lorem ipsum dolor sit amet, consectetur adipiscing elit, sed do eiusmod tempor incididunt ut labore et dolore magna aliqua. Ut enim ad minim veniam.</p>

<div class="service" style="left:73px">
  <div class="icon"><svg width="48" height="48" viewBox="0 0 48 48"><path d="M10 8c6-4 10 0 14 0s8-4 14 0c4 4 2 12 0 16l-2 18c-1 3-5 3-6 0l-3-12h-6l-3 12c-1 3-5 3-6 0l-2-18c-2-4-4-12 0-16z" fill="#f08a2e"/><path d="M18 16v14M24 16v12M30 16v14" stroke="#fff" stroke-width="2.5"/></svg></div>
  <h3>Root Canals</h3>
  <p>Lorem ipsum dolor sit amet, consectetur adipiscing elit, sed do eiusmod tempor</p>
  <span class="btn">READ MORE</span>
</div>
<div class="service" style="left:343px">
  <div class="icon"><svg width="48" height="48" viewBox="0 0 48 48"><path d="M10 6h28v14H10z" fill="#f08a2e"/><path d="M12 20c0 8 2 22 6 22 3 0 3-10 6-10s3 10 6 10c4 0 6-14 6-22" fill="none" stroke="#f08a2e" stroke-width="3"/></svg></div>
  <h3>Crowns</h3>
  <p>Lorem ipsum dolor sit amet, consectetur adipiscing elit, sed do eiusmod tempor</p>
  <span class="btn">READ MORE</span>
</div>
<div class="service" style="left:613px">
  <div class="icon"><svg width="48" height="48" viewBox="0 0 48 48"><path d="M8 12c5-4 9-1 13-1s8-3 13 1c4 4 2 11 0 15l-2 15c-1 3-5 3-6 0l-2-10h-6l-2 10c-1 3-5 3-6 0l-2-15c-2-4-4-11 0-15z" fill="#f08a2e"/><path d="M40 4l1.5 4 4 1.5-4 1.5-1.5 4-1.5-4-4-1.5 4-1.5z" fill="#f08a2e"/></svg></div>
  <h3>Tooth Whitening</h3>
  <p>Lorem ipsum dolor sit amet, consectetur adipiscing elit, sed do eiusmod tempor</p>
  <span class="btn">READ MORE</span>
</div>
<div class="service" style="left:883px">
  <div class="icon"><svg width="48" height="48" viewBox="0 0 48 48"><path d="M10 6c5-3 9 0 14 0s9-3 14 0c4 4 2 12 0 16l-2 18c-1 4-6 4-7 0l-1-10h-8l-1 10c-1 4-6 4-7 0l-2-18c-2-4-4-12 0-16z" fill="#f08a2e"/><path d="M24 20v20M20 24h8M20 29h8M20 34h8" stroke="#fff" stroke-width="2"/></svg></div>
  <h3>Implants</h3>
  <p>Lorem ipsum dolor sit amet, consectetur adipiscing elit, sed do eiusmod tempor</p>
  <span class="btn">READ MORE</span>
</div>

<section class="welcome">
  <h2>Welcome to Goldvale Dental Care</h2>
  <div class="rule"></div>
  <p class="tagline">If you listen to our patients they will tell you... it's our genuine care and gentle nature that sets us apart!</p>
  <p class="body">We want to provide you with everything you could want in a dental office: excellent work, a gentle nature, and a friendly staff - all in a comfortable location and at a great price. Dr Marlow, our dentist, combines many years of experience in the dental field, with her gentle and friendly personality. Over the course of her career, she has also worked with several Oral &amp; Maxillofacial Surgeons. Her experience enables her to excel at complex procedures that many dentists must refer out to other offices.</p>
  <span class="btn-ghost">READ MORE</span>
</section>

<h2 class="sec-title" style="top:1712px">Quotes</h2>
<p class="sec-lead" style="top:1766px">Lorem ipsum dolor sit amet, consectetur adipiscing elit, sed do eiusmod tempor incididunt ut labore et dolore magna aliqua. Ut enim ad minim veniam.</p>

<div class="quote" style="left:80px">I find that most men would rather have their bellies opened for five hundred dollars than have a tooth pulled for five.</div>
<div class="quote" style="left:440px">My health plan doesn't cover dental, so I enrolled my teeth as 32 dependents, each needing a complete physical</div>
<div class="quote" style="left:802px">Treat your password like your toothbrush. Don't let anybody else use it, and get a new one every six months</div>

<div class="author" style="left:80px"><div class="avatar" role="img" aria-label="Portrait of the quote author"></div>Elias Norwood</div>
<div class="author" style="left:440px"><div class="avatar" role="img" aria-label="Portrait of the quote author"></div>Henry Caldwell</div>
<div class="author" style="left:802px"><div class="avatar" role="img" aria-label="Portrait of the quote author"></div>Owen Pritchard</div>

<div class="divider"></div>

<h3 class="member-title">Member of:</h3>
<p class="member-text">Lorem ipsum dolor sit amet, consectetur adipiscing elit, sed do eiusmod tempor incididunt ut labore et dolore magna aliqua. Ut enim ad.</p>
<div class="badge" style="left:599px"><span></span></div>
<div class="badge" style="left:787px"><span></span></div>
<div class="badge" style="left:973px"><span></span></div>

<footer class="site-footer">
  <div class="brand"><span class="brand-dot"></span>Goldvale Dental Care</div>
  <p class="legal">(c) 2016, Goldvale dental care,<br>All Right Reserved. Privacy Policy,<br>Terms &amp; Conditions</p>

  <h4 class="col-title" style="left:358px">Useful Links</h4>
  <ul class="links">
    <li>Patient Health Library</li>
    <li>Residency &amp; Fellowship</li>
    <li>Information</li>
    <li>Nursing Professional</li>
    <li>Development</li>
    <li>Professional Training</li>
  </ul>

  <h4 class="col-title" style="left:614px">Contact Info</h4>
  <div class="info" style="top:100px"><svg width="13" height="16" viewBox="0 0 24 24"><path fill="#fff" d="M12 2a7 7 0 0 0-7 7c0 5.2 7 13 7 13s7-7.8 7-13a7 7 0 0 0-7-7zm0 9.5A2.5 2.5 0 1 1 12 6.5a2.5 2.5 0 0 1 0 5z"/></svg><span>4820 Orchard Row, CA 95390<br>(next to Sunfield Grocers)</span></div>
  <div class="info" style="top:160px"><svg width="13" height="14" viewBox="0 0 24 24"><path fill="#fff" d="M6.6 10.8a15.1 15.1 0 0 0 6.6 6.6l2.2-2.2c.3-.3.7-.4 1-.2 1.1.4 2.3.6 3.6.6.6 0 1 .4 1 1V20c0 .6-.4 1-1 1A17 17 0 0 1 3 4c0-.6.4-1 1-1h3.5c.6 0 1 .4 1 1 0 1.3.2 2.5.6 3.6.1.3 0 .7-.2 1z"/></svg><span>Call Us &nbsp;209-555-0148</span></div>
  <div class="info" style="top:182px"><svg width="13" height="12" viewBox="0 0 24 20"><path fill="#fff" d="M2 2h20v16H2z"/><path d="M2 3l10 8 10-8" fill="none" stroke="#6d6d6d" stroke-width="2"/></svg><span>Email &nbsp;info@goldvaledental.net</span></div>

  <h4 class="col-title" style="left:913px">Get In Touch</h4>
  <div class="field" style="top:97px">Enter Name</div>
  <div class="field" style="top:143px">Enter Email Address</div>
  <span class="btn submit">SUBMIT</span>
</footer>

</body>
</html>
```